Update Pulp Pantry menu board to appear Fresh and modern

I need a menu board design that is not cluttered, easy to read, playful and the style of healthy and fresh for a juice bar. I will be editing the details of the items, so basically the design is all I need. I prefer the files to be in Microsoft Publisher as I am most familiar, but I have illustrator as well, but not as advanced on that. The size should be 36"x36". I will create 3 seperate boards from the one design.

Target Market(s)

health concious people, active lifestyle people

Font styles to use
Serif

Colors

Designer to choose colors to be used in the design.

Requirements
Must have
• Not cluttered
• Modern feel
Nice to have
• i like the style of the
• "cold pressed juice" part of my attached juice bottle label

```html
<!DOCTYPE html>
<html lang="en">
<head>
<meta charset="utf-8">
<title>Pulp Pantry – Wraps &amp; Breakfast Menu</title>
<link rel="stylesheet" href="https://fonts.googleapis.com/css2?family=Josefin+Sans:wght@300&family=Alfa+Slab+One&family=Teko:wght@500&family=Open+Sans:wght@700&family=Oswald:wght@500&family=Montserrat:wght@800&display=swap">
<style>
  :root {
    --board: #231f20;
    --wood-light: #d9bd98;
    --wood-dark: #b08a62;
    --leaf: #3e6b2c;
    --pink: #e2137f;
    --orange: #f07a1a;
    --ink: #3a3a3a;
    --white: #ffffff;
    --tag-bg: #545454;
    --tag-text: #f3e21b;
    --rule: #bfbfbf;
  }
  * { margin: 0; padding: 0; box-sizing: border-box; }
  html, body { width: 1200px; height: 1200px; overflow: hidden; background: var(--board); }
  .menu-board { position: relative; width: 1200px; height: 1200px; overflow: hidden; }

  .wood-header {
    position: absolute; inset: 0 0 auto 0; height: 260px;
    background: linear-gradient(100deg, var(--wood-light) 0%, #e4cba8 30%, var(--wood-dark) 55%, #dcc19c 80%, var(--wood-light) 100%);
  }
  .foliage { position: absolute; top: 10px; height: 190px; width: 240px;
    background: radial-gradient(ellipse at center, rgba(62,107,44,.85) 0%, rgba(62,107,44,.35) 55%, rgba(62,107,44,0) 75%); }
  .foliage--left { left: 90px; }
  .foliage--right { right: 90px; }

  .board-shape { position: absolute; left: 0; top: 0; width: 1200px; height: 1200px; }

  .brand { position: absolute; left: 395px; top: 45px; display: flex; align-items: center; gap: 16px; }
  .brand__dot { width: 132px; height: 132px; border-radius: 50%; background: var(--orange); }
  .brand__name { font-family: "Montserrat", sans-serif; font-weight: 800; color: var(--white);
    font-size: 60px; line-height: 58px; letter-spacing: 1px; text-transform: uppercase; }

  .column { position: absolute; top: 232px; width: 330px; padding-left: 12px; border-left: 2px solid var(--rule); height: 878px; }
  .column--cold { left: 98px; }
  .column--warm { left: 444px; }
  .column--breakfast { left: 790px; border-left-width: 2px; }

  .section-title { color: var(--pink); margin-bottom: 26px; }
  .section-title__light { display: block; font-family: "Josefin Sans", sans-serif; font-weight: 300;
    font-size: 60px; line-height: 50px; letter-spacing: 3px; }
  .section-title__bold { display: block; font-family: "Alfa Slab One", serif;
    font-size: 58px; line-height: 58px; letter-spacing: 1px; }
  .section-title--stacked .section-title__bold { line-height: 54px; }

  .item { margin-bottom: 16px; }
  .item__name { font-family: "Teko", sans-serif; font-weight: 500; color: var(--pink);
    font-size: 31px; line-height: 28px; letter-spacing: .5px; text-transform: uppercase; }
  .item__desc { font-family: "Open Sans", sans-serif; font-weight: 700; color: var(--white);
    font-size: 12.6px; line-height: 16.4px; text-transform: uppercase; }
  .item__note { font-family: "Open Sans", sans-serif; font-weight: 700; color: var(--tag-text);
    font-size: 8.5px; line-height: 11px; }
  .prices { display: flex; gap: 8px; margin-top: 7px; }
  .price { width: 62px; text-align: center; }
  .price__size { display: block; background: var(--tag-bg); color: var(--tag-text);
    font-family: "Open Sans", sans-serif; font-weight: 700; font-size: 12px; line-height: 19px; }
  .price__amount { display: block; font-family: "Oswald", sans-serif; font-weight: 500; color: var(--white);
    font-size: 26px; line-height: 36px; }

  .served-all-day { font-family: "Montserrat", sans-serif; font-weight: 800; color: var(--pink);
    font-size: 27px; letter-spacing: 2px; margin-top: 22px; }
</style>
</head>
<body>
<main class="menu-board">
  <div class="wood-header" role="img" aria-label="Light wooden plank background with green leafy sprigs">
    <div class="foliage foliage--left"></div>
    <div class="foliage foliage--right"></div>
  </div>
  <svg class="board-shape" viewBox="0 0 1200 1200" aria-hidden="true">
    <path d="M0 232 Q600 0 1200 232 L1200 1200 L0 1200 Z" fill="var(--board)"/>
  </svg>

  <header class="brand">
    <span class="brand__dot" aria-hidden="true"></span>
    <h1 class="brand__name">Pulp<br>Pantry</h1>
  </header>

  <section class="column column--cold">
    <h2 class="section-title"><span class="section-title__light">COLD</span><span class="section-title__bold">WRAPS</span></h2>
    <article class="item">
      <h3 class="item__name">BLT Ranch Wrap</h3>
      <p class="item__desc">Roasted red pepper hummus,<br>kalamata olives, spring mix,<br>tomato on a wheat tortilla</p>
      <p class="item__note">Add Chicken to a Sm/Reg 1.50 &nbsp;Lrg 2.50</p>
      <div class="prices">
        <div class="price"><span class="price__size">Small</span><span class="price__amount">5</span></div>
        <div class="price"><span class="price__size">Regular</span><span class="price__amount">6.75</span></div>
        <div class="price"><span class="price__size">Large</span><span class="price__amount">8.75</span></div>
      </div>
    </article>
    <article class="item">
      <h3 class="item__name">Pesto Wrap</h3>
      <p class="item__desc">Grilled chicken breast, spring<br>mix, tomatoes, sun dried<br>tomato pesto</p>
      <div class="prices">
        <div class="price"><span class="price__size">Small</span><span class="price__amount">5</span></div>
        <div class="price"><span class="price__size">Regular</span><span class="price__amount">6.50</span></div>
        <div class="price"><span class="price__size">Large</span><span class="price__amount">8.25</span></div>
      </div>
    </article>
    <article class="item">
      <h3 class="item__name">Chicken Caesar</h3>
      <p class="item__desc">Grilled chicken breast, romaine<br>lettuce, parmesan, caesar<br>dressing</p>
      <div class="prices">
        <div class="price"><span class="price__size">Small</span><span class="price__amount">5</span></div>
        <div class="price"><span class="price__size">Regular</span><span class="price__amount">6.50</span></div>
        <div class="price"><span class="price__size">Large</span><span class="price__amount">8.25</span></div>
      </div>
    </article>
    <article class="item">
      <h3 class="item__name">Buffalo Chicken</h3>
      <p class="item__desc">Lightly breaded buffalo chicken,<br>mixed greens, tomato, ranch</p>
      <div class="prices">
        <div class="price"><span class="price__size">Small</span><span class="price__amount">5</span></div>
        <div class="price"><span class="price__size">Regular</span><span class="price__amount">6.50</span></div>
        <div class="price"><span class="price__size">Large</span><span class="price__amount">8.25</span></div>
      </div>
    </article>
    <article class="item">
      <h3 class="item__name">Greek Wrap</h3>
      <p class="item__desc">Roasted red pepper hummus,<br>kalamata olives, spring mix,<br>tomato on a wheat tortilla</p>
      <p class="item__note">Add Chicken to a Small 1.50 or Large 2.50</p>
      <div class="prices">
        <div class="price"><span class="price__size">Regular</span><span class="price__amount">4.75</span></div>
        <div class="price"><span class="price__size">Large</span><span class="price__amount">7.50</span></div>
      </div>
    </article>
  </section>

  <section class="column column--warm">
    <h2 class="section-title"><span class="section-title__light">WARM</span><span class="section-title__bold">WRAPS</span></h2>
    <article class="item">
      <h3 class="item__name">Cheese Steak Wrap</h3>
      <p class="item__desc">Thinly sliced beef, onions,<br>peppers and cheddar jack cheese</p>
      <div class="prices">
        <div class="price"><span class="price__size">Regular</span><span class="price__amount">7.50</span></div>
        <div class="price"><span class="price__size">Large</span><span class="price__amount">15</span></div>
      </div>
    </article>
    <article class="item">
      <h3 class="item__name">BBQ Chicken Wrap</h3>
      <p class="item__desc">Chicken breast, bacon, onion<br>strings, BBQ sauce and cheddar<br>jack cheese</p>
      <div class="prices">
        <div class="price"><span class="price__size">Regular</span><span class="price__amount">8</span></div>
        <div class="price"><span class="price__size">Large</span><span class="price__amount">15.50</span></div>
      </div>
    </article>
    <article class="item">
      <h3 class="item__name">Philly Chicken Wrap</h3>
      <p class="item__desc">Chicken breast, onions, peppers<br>and cheddar jack cheese</p>
      <div class="prices">
        <div class="price"><span class="price__size">Regular</span><span class="price__amount">6.75</span></div>
        <div class="price"><span class="price__size">Large</span><span class="price__amount">12.50</span></div>
      </div>
    </article>
    <article class="item">
      <h3 class="item__name">Venetian Chicken Wrap</h3>
      <p class="item__desc">Grilled chicken breast, roasted<br>red peppers, tomato, cheddar<br>jack cheese and sun dried<br>tomato pesto</p>
      <div class="prices">
        <div class="price"><span class="price__size">Regular</span><span class="price__amount">6.75</span></div>
        <div class="price"><span class="price__size">Large</span><span class="price__amount">12.50</span></div>
      </div>
    </article>
    <article class="item">
      <h3 class="item__name">Chicken &amp; Broccoli</h3>
      <p class="item__desc">Grilled chicken breast, steamed<br>broccoli and cheddar jack<br>cheese</p>
      <div class="prices">
        <div class="price"><span class="price__size">Regular</span><span class="price__amount">6.75</span></div>
        <div class="price"><span class="price__size">Large</span><span class="price__amount">12.50</span></div>
      </div>
    </article>
  </section>

  <section class="column column--breakfast">
    <h2 class="section-title section-title--stacked"><span class="section-title__bold">BREAK<br>FAST</span></h2>
    <article class="item">
      <h3 class="item__name">Bacon Burrito</h3>
      <p class="item__desc">Bacon, scrambled eggs,<br>potato, cheese with green chili</p>
      <div class="prices">
        <div class="price"><span class="price__size">Regular</span><span class="price__amount">5.50</span></div>
        <div class="price"><span class="price__size">Large</span><span class="price__amount">10</span></div>
      </div>
    </article>
    <article class="item">
      <h3 class="item__name">Sausage Burrito</h3>
      <p class="item__desc">Sausage, scrambled eggs,<br>potato, cheese, green chili</p>
      <div class="prices">
        <div class="price"><span class="price__size">Regular</span><span class="price__amount">5.50</span></div>
        <div class="price"><span class="price__size">Large</span><span class="price__amount">10</span></div>
      </div>
    </article>
    <article class="item">
      <h3 class="item__name">Meat &amp; Potatoes Burrito</h3>
      <p class="item__desc">Philly beef, scrambled eggs,<br>potato, cheese, green chili</p>
      <div class="prices">
        <div class="price"><span class="price__size">Regular</span><span class="price__amount">7.50</span></div>
        <div class="price"><span class="price__size">Large</span><span class="price__amount">15</span></div>
      </div>
    </article>
    <article class="item">
      <h3 class="item__name">Bean Breakfast Burrito</h3>
      <p class="item__desc">Scrambled eggs, refried beans,<br>green chili, potato, cheese</p>
      <div class="prices">
        <div class="price"><span class="price__size">Regular</span><span class="price__amount">5.50</span></div>
        <div class="price"><span class="price__size">Large</span><span class="price__amount">10</span></div>
      </div>
    </article>
    <article class="item">
      <h3 class="item__name">Veggie Omelet Burrito</h3>
      <p class="item__desc">Scrambled eggs, spinach, roasted<br>red peppers, tomato, cheese,<br>green chili on a wheat tortilla</p>
      <div class="prices">
        <div class="price"><span class="price__size">Regular</span><span class="price__amount">5.50</span></div>
        <div class="price"><span class="price__size">Large</span><span class="price__amount">10</span></div>
      </div>
    </article>
    <p class="served-all-day">SERVED ALL DAY</p>
  </section>
</main>
</body>
</html>
```